Harlow Pennick Group Business Cards

We have a new logo, and want to design new business cards with it. We are 21 years in business, and want a fresh but professional look, so not a lot of extra stuff on the card. We are a recruiting and staffing firm focused on placing accounting and finance professionals in the Dallas TX area. I've attached our new logo that should be displayed on the cards. Here is what I think we want on the cards:
Ned Varcombe, CPA
Partner and Managing Director
8262 Quarry Mill Rd.
Suite 610
Dallas, TX 75391
O 214-583-9071
M 214-690-1482
ned@harlowpennick-example.com
www.harlowpennick-example.com

```html
<!DOCTYPE html>
<html lang="en">
<head>
<meta charset="utf-8">
<title>Harlow Pennick Group Business Cards</title>
<link href="https://fonts.googleapis.com/css2?family=Open+Sans:wght@400;600;700&display=swap" rel="stylesheet">
<style>
  :root {
    --bg: #2a2a2c;
    --card: #1c1c1e;
    --blue: #2f56a6;
    --grey: #9a9a9e;
    --grey-light: #bfbfc3;
    --text-dim: #77777b;
  }
  * { margin: 0; padding: 0; box-sizing: border-box; }
  html, body { width: 1200px; height: 900px; overflow: hidden; }
  body {
    background: var(--bg);
    font-family: "Open Sans", sans-serif;
    display: flex;
    flex-direction: column;
    align-items: center;
    justify-content: center;
    gap: 50px;
  }
  .card {
    width: 630px;
    height: 360px;
    background: var(--card);
    position: relative;
  }
  .card-front {
    display: flex;
    flex-direction: column;
    align-items: center;
    justify-content: center;
  }
  .wordmark {
    color: var(--blue);
    font-weight: 700;
    font-size: 34px;
    letter-spacing: 1px;
    text-transform: uppercase;
  }
  .front-rule {
    width: 420px;
    height: 2px;
    background: var(--grey);
    margin-top: 12px;
  }
  .back-wordmark {
    position: absolute;
    left: 44px;
    top: 118px;
    width: 230px;
    color: var(--blue);
    font-weight: 700;
    font-size: 30px;
    line-height: 1.1;
    text-transform: uppercase;
  }
  .contact {
    position: absolute;
    left: 320px;
    top: 104px;
  }
  .person-name {
    color: var(--grey);
    font-size: 22px;
    font-weight: 400;
    text-transform: uppercase;
    letter-spacing: 0.5px;
  }
  .person-name .credential { font-size: 14px; }
  .person-title {
    color: var(--blue);
    font-size: 12px;
    font-weight: 700;
    text-transform: uppercase;
    letter-spacing: 0.5px;
    margin-bottom: 10px;
  }
  .contact-list { list-style: none; }
  .contact-list li {
    display: flex;
    align-items: center;
    gap: 10px;
    color: var(--text-dim);
    font-size: 14px;
    line-height: 25px;
  }
  .contact-list svg { width: 12px; height: 12px; fill: var(--blue); flex: none; }
  .address {
    position: absolute;
    left: 44px;
    bottom: 44px;
    color: var(--text-dim);
    font-size: 14px;
  }
</style>
</head>
<body>
  <section class="card card-front">
    <div class="wordmark">Harlow Pennick Group</div>
    <div class="front-rule"></div>
  </section>

  <section class="card card-back">
    <div class="back-wordmark">Harlow Pennick Group</div>
    <div class="contact">
      <div class="person-name">Ned Varcombe, <span class="credential">CPA</span></div>
      <div class="person-title">Partner and Managing Director</div>
      <ul class="contact-list">
        <li><svg viewBox="0 0 12 12"><path d="M2 1l2 0 1 3-1.5 1a7 7 0 0 0 3.5 3.5L8 7l3 1v2c0 .6-.4 1-1 1A9 9 0 0 1 1 2c0-.6.4-1 1-1z"/></svg>214-583-9071</li>
        <li><svg viewBox="0 0 12 12"><path d="M3 0h6a1 1 0 0 1 1 1v10a1 1 0 0 1-1 1H3a1 1 0 0 1-1-1V1a1 1 0 0 1 1-1zm0 2v7h6V2z"/></svg>214-690-1482</li>
        <li><svg viewBox="0 0 12 12"><path d="M0 2h12v8H0zm1 1v.5l5 3 5-3V3z"/></svg>ned@harlowpennick-example.com</li>
        <li><svg viewBox="0 0 12 12"><circle cx="6" cy="6" r="5.5"/></svg>www.harlowpennick-example.com</li>
      </ul>
    </div>
    <div class="address">8262 Quarry Mill Rd., Suite 610, Dallas, TX 75391</div>
  </section>
</body>
</html>
```